Flyer-Design für Restaurant umgeben von Wald und Wiesen
Die Designerin ist absolut zu empfehlen; sehr schnelle und kompetente Bearbeitung meiner Änderungswünsche, versteht offensichtlich ihr Handwerk und arbeitet sehr kundenorientiert. Auch bei Datenübergabe sehr hilfreiche Infos und Tips - danke vielmals!
Zielgruppe
Das Restaurant befindet sich auf dem Lande und ist umgeben von Wald und Wiesen. Das Gebäude selber ist historisch (17. Jh) und denkmalgeschützt. Wir übernehmen das Restaurant neu und sprechen durch eine Neugestaltung des Angebots und Verjüngung des Interieurs eine neue, jüngere Zielgruppe. Wir zeigen uns als junger, frischer und flexibler Anbieter auf dem regionalen Markt. Die Küche ist regional & saisonal,innovativ und modern, das Restaurant klar als Speiserestaurant positioniert.
Aufgabenstellung
Wir bieten saisonal wechselnde Specials an (Muttertagspacke, Häppli Hour, Wild Saison, Sylvester etc.), zu welchen wir jeweils einen Flyer erstellen möchten. Dazu brauchen wir eine Vorlage, die wir selbst in InDesign anpassen können. Das heißt, die Struktur des Flyers (Layout) soll bestehen bleiben, die Inhalte (Fotos/Illustration, Titel, Texte zum Angebot usw.) werden jeweils von uns selber abgeändert. Die Anlieferung des Flyers muss also offen erfolgen.
Frontseite: Logo, Titel, Illustration/Bild.....
Rückseite: Inhaltstext, Kontaktangaben, ev Illustration/Bild....
Format: A6 4-farbig, +je 3 mm Beschnitt, siehe Anhang
Botschaft/Stil: Entspannung, im Grünen, Frische, Geschmack, Simplizität, Unaufdringlich, Emotional
Logo: siehe Anhang
Beispielvorlage: Im Sommer bieten wir einen Häppli Hour, wo sich die Gäste gemütlich auf unseren Sitzsäcken im Garten entspannen können, zu jedem Apéro- Getränk erhalten sie gratis ein sommerliches Häppchen.

```html
<!DOCTYPE html>
<html lang="de">
<head>
<meta charset="utf-8">
<title>Häppli Hour – Flyer Vorder- und Rückseite</title>
<link rel="stylesheet" href="https://fonts.googleapis.com/css2?family=Questrial&display=swap">
<style>
  :root {
    --green: #8cbf2b;
    --green-dark: #76a81e;
    --green-light: #b9d96f;
    --white: #ffffff;
    --backdrop: #f2f2ef;
    --drink-top: #eef3e2;
    --drink-mid: #b8cf8a;
    --drink-low: #6f8f3a;
    --food-light: #f4e6c8;
    --food-mid: #d9a35a;
    --food-dark: #b86a3a;
  }
  * { margin: 0; padding: 0; box-sizing: border-box; }
  html, body {
    width: 1200px; height: 917px; overflow: hidden;
    background: var(--backdrop);
    font-family: "Questrial", "Century Gothic", sans-serif;
  }
  .sheet {
    position: absolute; top: 44px;
    width: 540px; height: 830px;
    overflow: hidden;
    background: var(--green);
    color: var(--white);
  }
  .sheet--front { left: 30px; }
  .sheet--back { left: 630px; }

  /* Front */
  .drink-photo {
    position: absolute; left: 0; top: 0; width: 540px; height: 600px;
    background: linear-gradient(170deg, var(--drink-top) 0%, var(--drink-mid) 45%, var(--drink-low) 100%);
  }
  .front-curves { position: absolute; left: 0; top: 0; width: 540px; height: 830px; }
  .title-band {
    position: absolute; top: 0; left: 452px; width: 72px; height: 590px;
    background: rgba(140, 191, 43, 0.88);
  }
  .title-vertical {
    position: absolute;
    font-size: 66px; line-height: 1; white-space: nowrap;
    transform: rotate(-90deg); transform-origin: left top;
    color: var(--white);
  }
  .sheet--front .title-vertical { left: 456px; top: 560px; }
  .brand {
    position: absolute; display: flex; align-items: center; gap: 12px;
    font-size: 22px; line-height: 1.1; color: var(--white);
  }
  .brand-dot { width: 34px; height: 34px; border-radius: 50%; background: var(--white); flex: none; }
  .sheet--front .brand { left: 34px; top: 560px; }
  .tagline {
    position: absolute; left: 34px; top: 648px;
    font-size: 31px; line-height: 1.18;
  }

  /* Back */
  .title-band--back {
    position: absolute; top: 0; left: 446px; width: 80px; height: 830px;
    background: var(--green-light);
  }
  .sheet--back .title-vertical { left: 452px; top: 600px; }
  .offer {
    position: absolute; left: 24px; top: 34px; width: 410px;
    text-align: center;
  }
  .offer-heading { font-size: 38px; font-weight: 400; margin-bottom: 24px; }
  .offer-text { font-size: 15.5px; line-height: 1.45; margin-bottom: 18px; }
  .offer-price { font-size: 34px; margin-top: 14px; }
  .back-curves { position: absolute; left: 0; top: 0; width: 540px; height: 830px; }
  .sheet--back .brand { left: 34px; top: 640px; }
  .contact {
    position: absolute; left: 34px; top: 716px;
    font-size: 12px; line-height: 1.45;
  }
</style>
</head>
<body>

<section class="sheet sheet--front">
  <div class="drink-photo" role="img" aria-label="Foto: zwei Gläser mit Minz-Limetten-Drink auf Eis"></div>
  <svg class="front-curves" viewBox="0 0 540 830" aria-hidden="false">
    <path d="M0 520 C 160 500, 330 470, 540 430 L540 830 L0 830 Z" fill="var(--green)"/>
    <path d="M540 560 C 380 570, 250 650, 215 830 L540 830 Z" fill="var(--white)"/>
    <path role="img" aria-label="Foto: Häppchen mit Jakobsmuschel und Kräutern" d="M540 578 C 395 590, 272 662, 238 830 L540 830 Z" fill="url(#foodFront)"/>
    <defs>
      <radialGradient id="foodFront" cx="0.6" cy="0.6" r="0.7">
        <stop offset="0" stop-color="var(--food-light)"/>
        <stop offset="0.55" stop-color="var(--food-mid)"/>
        <stop offset="1" stop-color="var(--food-dark)"/>
      </radialGradient>
    </defs>
  </svg>
  <div class="title-band"></div>
  <div class="title-vertical">Häppli Hour</div>
  <div class="brand"><span class="brand-dot"></span><span>Restaurant<br>Lindenhof</span></div>
  <p class="tagline">Entspannen und<br>genießen!<br>Zu jedem Drink<br>ein Häppli!</p>
</section>

<section class="sheet sheet--back">
  <div class="title-band--back"></div>
  <svg class="back-curves" viewBox="0 0 540 830">
    <path d="M540 600 C 410 610, 300 690, 262 830 L540 830 Z" fill="var(--white)"/>
    <path role="img" aria-label="Foto: Häppchen mit Jakobsmuschel und Kräutern" d="M540 618 C 420 630, 318 700, 284 830 L540 830 Z" fill="url(#foodBack)"/>
    <defs>
      <radialGradient id="foodBack" cx="0.6" cy="0.6" r="0.7">
        <stop offset="0" stop-color="var(--food-light)"/>
        <stop offset="0.55" stop-color="var(--food-mid)"/>
        <stop offset="1" stop-color="var(--food-dark)"/>
      </radialGradient>
    </defs>
  </svg>
  <div class="title-vertical">Häppli Hour</div>
  <div class="offer">
    <h2 class="offer-heading">Donnerstags ab 19:00</h2>
    <p class="offer-text">Sie erhalten:<br>Zu jedem Getränk servieren wir Ihnen ein frisches Häppchen aus unserer saisonalen Küche.</p>
    <p class="offer-text">Genießen Sie den Abend auf unseren Sitzsäcken im Garten, umgeben von Wald und Wiesen der Region.</p>
    <p class="offer-text">Unsere Küche verwendet regionale Zutaten und wechselt die kleinen Gerichte jede Woche neu.</p>
    <p class="offer-text">Reservieren Sie Ihren Platz am besten vorab, die Plätze im Garten sind begrenzt und schnell vergeben.</p>
    <p class="offer-price">00,00 Euro</p>
  </div>
  <div class="brand"><span class="brand-dot"></span><span>Restaurant<br>Lindenhof</span></div>
  <p class="contact">Adresse, Telefon etc.<br>Dorfstrasse 12, 8000 Musterdorf<br>Telefon 000 000 00 00<br>info@lindenhof-beispiel.ch</p>
</section>

</body>
</html>
```